New Fun, Positive, energised looking Business Card Needed for High Achiever Coach

I am looking for a two sided full colour business card. I am self employed and have recently re branded my 1-2-1 work re-vitalising high achievers. My target client base for these cards is therefore high achievers - usually aged 40 -55, they are often entrepreneurs, CEO or work in banking and finance and 2/3 are male. I work with them on 90 day or 6 month coaching programs to help them live their success in a healthier, more sustainable and fulfiiled way. They pay for this privately so though they are corporate types the cards need not look 'corporate'. I want to portray the idea of transformation, vitality and re-connecting.
You can get a feel for the look I like on my new website: corinvale.co.uk
I want to use this logo with strapline (Re-Vitalising High Achievers) (I purchased off Logoharbor) and font/ colours (the turquoise and green).
Details to include on the card:
www.corinvale.co.uk
+44 7915 264318
mira@corinvale.co.uk
skype: miracorin
I'd also like to include:
Do you struggle to switch off? Want to be healthier and feel fitter? Want closer relationships? More clarity over the direction you are headed? I can help you do these things using integrated mind-body techniques. Visit corinvale.co.uk TODAY to apply for a FREE Breakthrough session.
BUT if that is too much text for a card I am open to advice/ammendments.
Updates
Thanks for your design - I am considering them. PLease change the wording to :

```html
<!DOCTYPE html>
<html lang="en">
<head>
<meta charset="utf-8">
<title>Mira Corin – Business Card</title>
<link rel="stylesheet" href="https://fonts.googleapis.com/css2?family=Rammetto+One&family=Dancing+Script:wght@500&family=Raleway:wght@400;500&display=swap">
<style>
  :root {
    --turquoise: #1fa3c9;
    --card: #f4f5f9;
    --ink: #6c6f78;
    --photo-light: #d9d9d9;
    --photo-dark: #5b5b5b;
    --backdrop: #e3e5ea;
  }
  * { box-sizing: border-box; margin: 0; padding: 0; }
  html, body {
    width: 1200px; height: 750px; overflow: hidden;
    background: var(--backdrop);
  }
  .sheet {
    position: relative; width: 1200px; height: 750px;
    display: flex; align-items: center; justify-content: center; gap: 60px;
  }
  .card {
    position: relative; background: var(--card); overflow: hidden;
    box-shadow: 0 6px 18px rgba(0,0,0,0.15);
  }

  /* Front */
  .card--front { width: 700px; height: 350px; }
  .front__photo {
    position: absolute; top: 0; right: 0; width: 62%; height: 100%;
    background:
      linear-gradient(90deg, var(--card) 0%, rgba(244,245,249,0) 30%),
      radial-gradient(ellipse at 65% 45%, var(--photo-light) 0%, #a8a8a8 45%, var(--photo-dark) 100%);
  }
  .front__text { position: absolute; top: 34px; left: 36px; width: 370px; }
  .name {
    font-family: "Rammetto One", sans-serif;
    color: var(--turquoise); line-height: 1; white-space: nowrap;
  }
  .front__text .name { font-size: 40px; }
  .strapline {
    font-family: "Dancing Script", cursive; font-weight: 500;
    color: var(--turquoise); white-space: nowrap;
  }
  .front__text .strapline { font-size: 27px; margin: 4px 0 0 30px; }
  .pitch {
    font-family: "Raleway", sans-serif; font-size: 10.5px; line-height: 1.55;
    letter-spacing: 0.06em; text-transform: uppercase; color: var(--ink);
    margin: 16px 0 0 30px;
  }

  /* Back */
  .card--back {
    width: 330px; height: 460px;
    display: flex; flex-direction: column; align-items: center;
  }
  .brand {
    margin-top: 92px; height: 56px;
    display: flex; align-items: center; gap: 12px;
    font-family: "Raleway", sans-serif; font-weight: 500; font-size: 22px;
    letter-spacing: 0.08em; color: var(--turquoise);
  }
  .brand__square { width: 18px; height: 18px; background: var(--turquoise); }
  .card--back .name { font-size: 36px; margin-top: 70px; }
  .card--back .strapline { font-size: 24px; margin-top: 4px; }
  .contact {
    list-style: none; margin-top: 26px; text-align: center;
    font-family: "Raleway", sans-serif; font-size: 12px; line-height: 1.7;
    letter-spacing: 0.1em; text-transform: uppercase; color: var(--ink);
  }
</style>
</head>
<body>
<main class="sheet">
  <section class="card card--front">
    <div class="front__photo" role="img" aria-label="Black and white photo of the coach speaking with a headset, gesturing with a pen"></div>
    <div class="front__text">
      <h1 class="name">Mira Corin</h1>
      <p class="strapline">Re-Vitalising High Achievers</p>
      <p class="pitch">Do you struggle to switch off? Want to be healthier and feel fitter? Want closer relationships? More clarity over the direction you are headed? I can help you do these things using integrated mind-body techniques. Visit corinvale.co.uk today to apply for a free breakthrough session.</p>
    </div>
  </section>

  <section class="card card--back">
    <div class="brand">
      <span class="brand__square" aria-hidden="true"></span>
      <span class="brand__name">Mira Corin</span>
    </div>
    <h2 class="name">Mira Corin</h2>
    <p class="strapline">Re-Vitalising High Achievers</p>
    <ul class="contact">
      <li>www.corinvale.co.uk</li>
      <li>+44 7915 264318</li>
      <li>mira@corinvale.co.uk</li>
      <li>skype: miracorin</li>
    </ul>
  </section>
</main>
</body>
</html>
```